Web design for new streaming audio service

We need a homepage design for a new streaming audio service. Our company is called Olvantra, and we’re basically Vidorama for Audiobooks, Stand-Up Comedy, Lectures, Language Learning, etc. Essentially like Tunelark for everything audio EXCEPT music.
You don’t have to code the homepage (Design Only), but it should include 3 different designs to work with 1) Web; 2) Phones; 3) Tablets.
Below is a link to a mockup of the web version which gives a good idea of what elements we want. This is just a mockup and we want you to improve it.
Once you download the mockup, please refer to the more detailed instructions below:
The following outlines the design project for the Olvantra homepage. We have provided a rough mockup of the homepage layout that gives you a general idea of what we’re going for. There are a few elements that we are attached to, and many others where you have complete creative freedom to do whatever you think looks good.
The ZIP file includes the following:
* Mockup to see what we have in mind (olvantra-homepage-mockup.jpg)
* Text used (olvantra-homepage-text.txt)
* Raw image of actor (olvantra-actor1.jpg)
* Raw images for samples (olvantra-sample-[name].jpg)
Although we have only provided a mockup layout for the web version, we also need you to provide a mobile phone and a tablet version of the design also. It’s very possible the tablet version may be substantially similar to the web version, but the mobile phone version will likely be much different.
All of the raw files are included in the attached ZIP file. Please use our photographs and text as provided although cropping, sizing, etc. is flexible per the instructions below.
Display Requirements:
* Web Version - Minimum resolution 1024x768 (72 dpi) but should look good on 1920x1080 (72 dpi) - Page should be designed to scale to look acceptable in all resolutions in between.
* Phone Version - Minimum Zentro 4 - 640x960 (326 dpi) but should look good on Korvel Nimbus Q5 - 1920x1080 (441 dpi) - Page should be designed to scale to look acceptable in all resolutions and devices in between.
* Tablet Version - Minimum Pagewick Ember LX 7” - 1280x800 (216 dpi) but should also look good on a Slato Breeze - 2048x1536 (264 dpi) - Page should be designed to scale to look acceptable in all resolutions and devices in between.
Above the Fold - We want to make sure the Olvantra logo, Member Login Link, Large Photo, Headline, Price, Button, and the first row of sample images are all “Above the fold”. As a general guideline, this means 600 pixels high on a 1024x768 72 dpi web screen. This requirement is less important on Phone versions.
Top Logo Bar - We want to retain the blue bar with the Olvantra logo on the page, although we are open to a different size, shape and positioning if it greatly enhances the design. Please use the standard logo color, although you are welcome to use either the horizontal or vertical orientation of the logo based on your design.
Text color, font and size - Feel free to design the text in anyway you choose as long as the text is readable on the target platforms.
Buttons - Feel free to use any size, shape and colors for the buttons as long as they are obvious and clickable relative to the page. The only exception is the Chatterly button should follow the Chatterly color scheme and logo treatment (the mockup doesn’t seem 100% correct.)
Top Photograph - We want to retain the large photograph across the top of the screen although final shape and dimensions are flexible.
Size and shape of content samples (i.e. Audiobooks, Stand-Up Comedy, etc.) - Feel free to design the content samples in anyway you choose.
Three Sales Points (i.e. Listen on your Zentro…, All you can enjoy…, etc.) - The Three Sales Points are envisioned to each have a corresponding illustration which you should provide and have rights for. The placeholder is represented by a square next to the text. The color size and shape of these elements are flexible and can be designed in any way you choose.
Opt-in form - Feel free to design the opt-in form in anyway you choose as long as the text is readable and the interactivity is obvious on the target platforms.
Text links and copyright notice - Feel free to design the bottom of the page text links and copyright notice in anyway you choose.
Additional colors, graphic design elements, etc. - Feel free to use any additional colors, graphic design elements, etc. to support your design.

```html
<!DOCTYPE html>
<html lang="en">
<head>
<meta charset="utf-8">
<title>Olvantra — Unlimited Listening</title>
<link href="https://fonts.googleapis.com/css2?family=Open+Sans:wght@300;400;600;700&display=swap" rel="stylesheet">
<style>
  :root {
    --page-bg: #ffffff;
    --top-strip: #e6e7e8;
    --brand-blue: #6aa9d4;
    --navy: #1f4f7c;
    --link-blue: #4f93c8;
    --orange: #f7a236;
    --orange-dark: #e58d1c;
    --sample-bg: #ededee;
    --heading-grey: #5a5c5e;
    --label-dark: #333538;
    --white: #ffffff;
  }
  * { box-sizing: border-box; margin: 0; padding: 0; }
  html, body {
    width: 1200px; height: 851px; overflow: hidden;
    background: var(--page-bg);
    font-family: "Open Sans", Arial, sans-serif;
  }
  .page { position: relative; width: 1200px; height: 851px; }

  .top-strip { height: 22px; background: var(--top-strip); }

  .hero { position: relative; height: 400px; background: var(--white); }
  .hero-photo {
    position: absolute; left: 0; top: 0; width: 760px; height: 100%;
    background:
      linear-gradient(90deg, rgba(255,255,255,0) 55%, #ffffff 100%),
      linear-gradient(180deg, #c9a58b 0%, #b98f74 35%, #8e8f9a 70%, #6f7e95 100%);
  }

  .brand-bar {
    position: absolute; left: 0; top: 0; width: 100%; height: 62px;
    background: var(--brand-blue);
    display: flex; align-items: center;
  }
  .brand {
    position: absolute; left: 230px; top: 50%; transform: translateY(-50%);
    display: flex; align-items: center; gap: 8px;
    color: var(--white); font-weight: 600; font-size: 22px; letter-spacing: -0.2px;
  }
  .brand-dot { width: 22px; height: 22px; border-radius: 50%; background: var(--white); }
  .member-login {
    position: absolute; left: 745px; top: 50%; transform: translateY(-50%);
    display: flex; align-items: center; gap: 8px;
    padding: 7px 14px; border: 1px solid rgba(255,255,255,0.85);
    color: var(--white); font-size: 13px; font-weight: 600; text-decoration: none;
  }
  .menu-icon { position: absolute; right: 32px; top: 50%; transform: translateY(-50%); }

  .hero-offer {
    position: absolute; left: 660px; top: 130px; width: 360px; text-align: center;
  }
  .headline {
    color: var(--navy); font-weight: 700; font-size: 27px; line-height: 1.2;
  }
  .price { margin-top: 30px; color: var(--navy); font-size: 13px; }
  .cta {
    display: inline-block; margin-top: 4px; padding: 9px 16px;
    background: var(--orange); border-bottom: 2px solid var(--orange-dark);
    color: var(--white); font-weight: 700; font-size: 18px; text-decoration: none;
  }
  .cta-note { margin-top: 4px; color: var(--link-blue); font-size: 11px; }

  .samples {
    height: 429px; background: var(--sample-bg);
    padding-top: 42px; text-align: center;
  }
  .samples-heading { color: var(--heading-grey); font-weight: 300; font-size: 29px; }
  .sample-row {
    margin-top: 40px; display: flex; justify-content: center; gap: 38px;
  }
  .sample { width: 160px; }
  .sample-cover { width: 160px; height: 165px; box-shadow: 0 2px 4px rgba(0,0,0,0.15); }
  .cover-audiobooks { background: linear-gradient(180deg, #2f4f5c, #18262c); }
  .cover-comedy { background: linear-gradient(180deg, #c9a98e, #7d8d55); }
  .cover-language { background: linear-gradient(180deg, #2aa6e8, #1a6fb8); }
  .cover-memoirs { background: linear-gradient(180deg, #c8c3bd, #8fbf6a); }
  .sample-label {
    margin-top: 12px; color: var(--label-dark); font-weight: 600; font-size: 14px;
  }
</style>
</head>
<body>
<div class="page">
  <div class="top-strip"></div>

  <header class="hero">
    <div class="hero-photo" role="img" aria-label="Photo of a smiling young man wearing headphones, listening on his phone"></div>

    <div class="brand-bar">
      <div class="brand"><span class="brand-dot"></span>Olvantra</div>
      <a class="member-login" href="#">
        <svg width="10" height="13" viewBox="0 0 10 13" aria-hidden="true">
          <rect x="1" y="5.5" width="8" height="7" fill="none" stroke="#fff" stroke-width="1.3"/>
          <path d="M2.8 5.5V3.6a2.2 2.2 0 0 1 4.4 0v1.9" fill="none" stroke="#fff" stroke-width="1.3"/>
        </svg>
        Member Login
      </a>
      <svg class="menu-icon" width="26" height="18" viewBox="0 0 26 18" aria-label="Menu">
        <rect y="0" width="26" height="2.4" fill="#fff"/>
        <rect y="7.8" width="26" height="2.4" fill="#fff"/>
        <rect y="15.6" width="26" height="2.4" fill="#fff"/>
      </svg>
    </div>

    <div class="hero-offer">
      <h1 class="headline">Unlimited Listening.<br>Wherever you are.</h1>
      <p class="price">Only $9.99 per month</p>
      <a class="cta" href="#">Start Your Free Trial</a>
      <p class="cta-note">* Credit Card Not Required</p>
    </div>
  </header>

  <section class="samples">
    <h2 class="samples-heading">A sample of what you can listen to on Olvantra</h2>
    <div class="sample-row">
      <div class="sample">
        <div class="sample-cover cover-audiobooks" role="img" aria-label="Audiobook cover artwork"></div>
        <p class="sample-label">Audiobooks</p>
      </div>
      <div class="sample">
        <div class="sample-cover cover-comedy" role="img" aria-label="Stand-up comedy album cover artwork"></div>
        <p class="sample-label">Stand-Up Comedy</p>
      </div>
      <div class="sample">
        <div class="sample-cover cover-language" role="img" aria-label="French language course cover artwork"></div>
        <p class="sample-label">Language Learning</p>
      </div>
      <div class="sample">
        <div class="sample-cover cover-memoirs" role="img" aria-label="Biography cover artwork"></div>
        <p class="sample-label">Biographies &amp; Memoirs</p>
      </div>
    </div>
  </section>
</div>
</body>
</html>
```